25kg bag for branded milk powder

We are looking for an attractive bag for our Holland dairy milk powder range. We will have 5 kinds of products.

Instant Full Cream milk powder
Full cream milk powder
Instant fat filled milk powder
Skimmed milk powder
Dairy ingredients

The bags are standard industrial 25kg kraft multiply paper bags with inner poly linner.

We want to have an hormonized design where each type of dairy product is differentiated by the product name and a color,

Please see attached design as reference.

Target Market(s)

Middle East and Africa

Font styles to use
Sans Serif

Requirements
Must have
• The bags must show that we are a dutch company and have a profesional feel.
• We want a general design that will be differentiated by colour coding.
• We want the design to be less conservative compared to the attached examples.
• The bags must be easilly recognisable from all sides as for picture of Vorlund Creameries branded bags on pallets attached.
• We have also attached some bags design templates as a reference.
Nice to have
• We would like to use sybols or imagery that symbolises Dutch origin and quality
Should not have
• We cannot have too many images to keep it simple.

```html
<!DOCTYPE html>
<html lang="en">
<head>
<meta charset="utf-8">
<title>Meridale Dairy Foods – Full Cream Milk Powder 25 kg bag</title>
<link href="https://fonts.googleapis.com/css2?family=Open+Sans:wght@400;600;700&family=Yellowtail&display=swap" rel="stylesheet">
<style>
  :root{
    --bag-red:#e31b25;
    --bag-orange:#fb9432;
    --bag-orange-mid:#f2582a;
    --bag-back-glow:#f0432a;
    --panel-line:#3a1f1f;
    --dim-line:#222222;
    --logo-white:#ffffff;
    --logo-text:#3b3b3b;
    --logo-dot:#f6cf3c;
    --script-red:#d8232a;
    --ink:#111111;
    --label-white:#ffffff;
    --milk-white:#fbfbfd;
    --milk-mid:#eef0f4;
    --milk-shade:#d7dbe2;
    --glass-light:#ffffff;
    --glass-mid:#e2eeee;
    --glass-shade:#b9cccc;
  }
  html,body{margin:0;padding:0;width:1200px;height:1090px;overflow:hidden;background:#ffffff;}
  .bag-artwork{display:block;width:1200px;height:1090px;}
  .dim-label{font-family:'Open Sans',sans-serif;font-size:13px;fill:var(--dim-line);}
  .dim-line{stroke:var(--dim-line);stroke-width:1.2;fill:none;}
  .panel-line{stroke:var(--panel-line);stroke-width:1;fill:none;opacity:.75;}
  .logo-card{fill:var(--logo-white);}
  .logo-name{font-family:'Open Sans',sans-serif;font-weight:600;fill:var(--logo-text);}
  .logo-dot{fill:var(--logo-dot);}
  .product-name{font-family:'Yellowtail',cursive;fill:var(--script-red);}
  .net-weight{font-family:'Open Sans',sans-serif;fill:var(--ink);}
  .info-text{font-family:'Open Sans',sans-serif;fill:var(--label-white);}
</style>
</head>
<body>
<svg class="bag-artwork" viewBox="0 0 1300 1181" preserveAspectRatio="none" xmlns="http://www.w3.org/2000/svg">
  <defs>
    <radialGradient id="front-glow" cx="490" cy="650" r="560" gradientUnits="userSpaceOnUse">
      <stop offset="0" stop-color="var(--bag-orange)"/>
      <stop offset=".45" stop-color="var(--bag-orange-mid)"/>
      <stop offset="1" stop-color="var(--bag-red)"/>
    </radialGradient>
    <radialGradient id="back-glow" cx="1000" cy="560" r="420" gradientUnits="userSpaceOnUse">
      <stop offset="0" stop-color="var(--bag-back-glow)"/>
      <stop offset="1" stop-color="var(--bag-red)"/>
    </radialGradient>
    <radialGradient id="milk-splash" cx="470" cy="400" r="220" gradientUnits="userSpaceOnUse">
      <stop offset="0" stop-color="var(--milk-white)"/>
      <stop offset=".75" stop-color="var(--milk-mid)"/>
      <stop offset="1" stop-color="var(--milk-shade)"/>
    </radialGradient>
    <linearGradient id="milk-glass" x1="0" y1="0" x2="1" y2="1">
      <stop offset="0" stop-color="var(--glass-light)"/>
      <stop offset=".6" stop-color="var(--glass-mid)"/>
      <stop offset="1" stop-color="var(--glass-shade)"/>
    </linearGradient>
  </defs>

  <!-- dimension marks -->
  <g class="dimensions">
    <path class="dim-line" d="M61 40H1258 M61 33V48 M82 33V48 M190 33V48 M778 33V48 M1258 33V48"/>
    <text class="dim-label" x="85" y="26" text-anchor="middle">20 mm</text>
    <text class="dim-label" x="150" y="26" text-anchor="middle">100 mm</text>
    <text class="dim-label" x="437" y="26" text-anchor="middle">550 mm</text>
    <text class="dim-label" x="1040" y="26" text-anchor="middle">450 mm</text>
    <path class="dim-line" d="M35 72V1116 M28 72H44 M28 978H44 M28 1116H44"/>
    <text class="dim-label" transform="translate(24 655) rotate(-90)" text-anchor="middle">850 mm</text>
    <text class="dim-label" transform="translate(24 1045) rotate(-90)" text-anchor="middle">130 mm</text>
  </g>

  <!-- bag surface -->
  <g class="bag-surface">
    <rect x="45" y="56" width="1226" height="1086" fill="var(--bag-red)"/>
    <rect x="45" y="56" width="785" height="1086" fill="url(#front-glow)"/>
    <rect x="830" y="56" width="441" height="1086" fill="url(#back-glow)"/>
  </g>

  <!-- fold and panel lines -->
  <g class="panel-lines">
    <rect class="panel-line" x="61" y="72" width="1197" height="906"/>
    <path class="panel-line" d="M82 72V978 M138 72V978 M190 72V978 M242 72V978 M726 72V978 M778 72V978 M830 72V978"/>
    <rect class="panel-line" x="242" y="978" width="484" height="140"/>
  </g>

  <!-- artwork areas -->
  <circle role="img" aria-label="Milk splash illustration" cx="490" cy="430" r="205" fill="url(#milk-splash)"/>
  <path role="img" aria-label="Glass of milk with splashing milk illustration"
        d="M244 978 V820 C250 770 300 750 360 755 C440 762 520 800 560 840 C590 870 590 900 540 915 L510 978 Z"
        fill="url(#milk-glass)"/>

  <!-- product name -->
  <text class="product-name" x="486" y="395" font-size="66" text-anchor="middle" textLength="250" lengthAdjust="spacingAndGlyphs">Full Cream</text>
  <text class="product-name" x="486" y="478" font-size="66" text-anchor="middle" textLength="310" lengthAdjust="spacingAndGlyphs">Milk Powder</text>

  <text class="net-weight" x="617" y="758" font-size="36" text-anchor="middle">Net Weight:</text>
  <text class="net-weight" x="617" y="803" font-size="44" font-weight="700" text-anchor="middle">25 kg</text>

  <!-- top tabs -->
  <g class="logo-tab">
    <path class="logo-card" d="M254 56H480V167Q480 175 472 175H262Q254 175 254 167Z"/>
    <circle class="logo-dot" cx="290" cy="118" r="14"/>
    <text class="logo-name" x="385" y="112" font-size="24" text-anchor="middle">Meridale</text>
    <text class="logo-name" x="385" y="142" font-size="17" text-anchor="middle" letter-spacing="2">Dairy Foods</text>
  </g>
  <g class="certificate-tab">
    <path class="logo-card" d="M592 56H712V165Q712 173 704 173H600Q592 173 592 165Z"/>
    <circle role="img" aria-label="Certification badge" cx="652" cy="120" r="36" fill="#1e2a44"/>
  </g>

  <!-- gusset logos -->
  <g class="gusset-logo">
    <rect class="logo-card" x="140" y="358" width="102" height="256" rx="6"/>
    <g transform="translate(191 486) rotate(90)">
      <circle class="logo-dot" cx="-100" cy="0" r="13"/>
      <text class="logo-name" x="10" y="-6" font-size="24" text-anchor="middle">Meridale</text>
      <text class="logo-name" x="10" y="24" font-size="16" text-anchor="middle" letter-spacing="2">Dairy Foods</text>
    </g>
  </g>
  <g class="gusset-logo">
    <rect class="logo-card" x="727" y="366" width="102" height="256" rx="6"/>
    <g transform="translate(778 494) rotate(-90)">
      <circle class="logo-dot" cx="-100" cy="0" r="13"/>
      <text class="logo-name" x="10" y="-6" font-size="24" text-anchor="middle">Meridale</text>
      <text class="logo-name" x="10" y="24" font-size="16" text-anchor="middle" letter-spacing="2">Dairy Foods</text>
    </g>
  </g>

  <!-- bottom logo -->
  <g class="bottom-logo">
    <rect class="logo-card" x="348" y="998" width="245" height="110" rx="6"/>
    <circle class="logo-dot" cx="392" cy="1052" r="15"/>
    <text class="logo-name" x="492" y="1047" font-size="27" text-anchor="middle">Meridale</text>
    <text class="logo-name" x="492" y="1080" font-size="18" text-anchor="middle" letter-spacing="2">Dairy Foods</text>
  </g>

  <!-- back panel -->
  <g class="back-logo">
    <rect class="logo-card" x="920" y="318" width="208" height="93" rx="6"/>
    <circle class="logo-dot" cx="958" cy="362" r="13"/>
    <text class="logo-name" x="1045" y="360" font-size="23" text-anchor="middle">Meridale</text>
    <text class="logo-name" x="1045" y="389" font-size="15" text-anchor="middle" letter-spacing="2">Dairy Foods</text>
  </g>

  <g class="ingredients">
    <text class="info-text" x="920" y="451" font-size="22">Ingredients:</text>
    <text class="info-text" x="920" y="488" font-size="18" font-weight="700" letter-spacing="1">.................................</text>
    <text class="info-text" x="920" y="524" font-size="18" font-weight="700" letter-spacing="1">.................................</text>
    <text class="info-text" x="920" y="560" font-size="18" font-weight="700" letter-spacing="1">.................................</text>
  </g>

  <g class="production-info">
    <text class="info-text" x="854" y="893" font-size="16">Batch No:</text>
    <text class="info-text" x="854" y="914" font-size="16">Lot No:</text>
    <text class="info-text" x="854" y="934" font-size="16">Date of Production:</text>
    <path d="M1045 880V936" stroke="var(--label-white)" stroke-width="2"/>
    <text class="info-text" x="1074" y="862" font-size="16">Produced by:</text>
    <text class="info-text" x="1074" y="886" font-size="16">Meridale Dairy Foods</text>
    <text class="info-text" x="1074" y="912" font-size="16">Address...............</text>
    <text class="info-text" x="1074" y="934" font-size="16">............................</text>
    <text class="info-text" x="1074" y="953" font-size="16">Tel:.......................</text>
  </g>
</svg>
</body>
</html>
```